Luxury Business Card Design for High-End Window Treatments

Gilded Vantages
Custom Plantation Shutters & Architectural Shading Systems

⸻

BACK

Daniel Forsythe
Owner

Custom Interior & Exterior Window Treatments

919-482-7034
gildedvantages.com

I have included a picture that I’m hoping we can use on the back, but I’m also wondering if you can get rid of the ladder? Should we get rid of shutters , shades and blinds underneath Gilded Vantages?

Target Market(s)

High-end residential homeowners, custom home builders, architects, interior designers, and luxury renovation clients seeking premium plantation shutters and motorized architectural shading systems.

Industry/Entity Type

Custom Window treatments

Contact Information for Business Card

Front Gilded Vantages Custom Plantation Shutters Motorized Architectural Shading Systems BACK Daniel Forsythe Owner 919-482-7034 GildedVantages.com Custom Interior & Exterior Window Treatments By Appointment

Requirements
Nice to have
• Not 100% sure on nice to halves or the color but you can definitely check out my website to get a better understanding of what I’m trying to do

```html
<!DOCTYPE html>
<html lang="en">
<head>
<meta charset="utf-8">
<title>Gilded Vantages — Business Cards</title>
<link rel="stylesheet" href="https://fonts.googleapis.com/css2?family=Arvo:wght@700&family=Open+Sans:wght@300;400;700&display=swap">
<style>
  :root {
    --paper: #e9e9e8;
    --card-black: #151515;
    --gold: #e3c24f;
    --gold-deep: #c79a2b;
    --gold-edge: #b8921f;
    --cream: #e8e4d8;
    --grey-text: #c9c9c9;
    --photo-dark: #2c2c2c;
    --photo-mid: #555;
  }
  * { box-sizing: border-box; margin: 0; padding: 0; }
  html, body { width: 1200px; height: 801px; overflow: hidden; }
  body {
    background: var(--paper);
    font-family: "Open Sans", Arial, sans-serif;
    display: flex;
    align-items: center;
    justify-content: center;
    gap: 50px;
  }
  .card {
    position: relative;
    width: 540px;
    height: 309px;
    background: var(--card-black);
    border-bottom: 4px solid var(--gold-edge);
    border-right: 3px solid var(--gold-edge);
    box-shadow: 0 10px 24px rgba(0,0,0,.25);
    overflow: hidden;
    color: var(--cream);
  }
  /* Contact side */
  .brand-name {
    position: absolute;
    left: 34px; top: 42px;
    font-weight: 300;
    font-size: 40px;
    line-height: 1;
    color: var(--cream);
  }
  .offerings {
    position: absolute;
    font-family: "Arvo", Georgia, serif;
    font-weight: 700;
    color: var(--gold);
    display: flex;
    gap: 18px;
  }
  .card-contact .offerings { left: 36px; top: 96px; font-size: 16px; }
  .emblem-circle {
    position: absolute;
    right: 70px; top: 26px;
    width: 140px; height: 140px;
    border-radius: 50%;
    background: radial-gradient(circle at 40% 35%, #3a3a3a, #1d1d1d 70%);
  }
  .person-name {
    position: absolute;
    left: 36px; top: 146px;
    font-weight: 700;
    font-size: 20px;
    letter-spacing: .5px;
    color: var(--gold);
    text-transform: uppercase;
  }
  .person-role {
    position: absolute;
    left: 36px; top: 174px;
    font-size: 15px;
    color: var(--grey-text);
  }
  .divider {
    position: absolute;
    left: 36px; right: 36px; top: 204px;
    height: 1px;
    background: var(--gold-deep);
  }
  .contact-list {
    position: absolute;
    left: 36px; top: 218px;
    list-style: none;
    font-size: 15px;
    color: var(--grey-text);
    line-height: 1.65;
  }
  .contact-list li { display: flex; align-items: center; gap: 8px; }
  .contact-list svg { width: 13px; height: 13px; }
  .tagline-services {
    position: absolute;
    right: 36px; top: 220px;
    text-align: right;
    font-size: 14px;
    line-height: 1.35;
    color: var(--grey-text);
  }
  /* Photo side */
  .photo-fill {
    position: absolute; inset: 0;
    background: linear-gradient(160deg, var(--photo-mid) 0%, var(--photo-dark) 55%, #3e3e3e 100%);
  }
  .card-photo .brand-name {
    left: 0; right: 0; top: 78px;
    text-align: center;
    font-size: 50px;
  }
  .card-photo .offerings {
    left: 0; right: 0; top: 148px;
    justify-content: center;
    gap: 30px;
    font-size: 22px;
  }
  .gold-band {
    position: absolute;
    left: 40px; right: 40px; bottom: 26px;
    padding: 10px 0;
    background: linear-gradient(90deg, rgba(199,154,43,0) 0%, var(--gold-deep) 25%, var(--gold) 75%, rgba(227,194,79,.3) 100%);
    text-align: center;
    color: #2a2a2a;
    font-size: 15px;
    line-height: 1.3;
  }
</style>
</head>
<body>

  <article class="card card-contact">
    <div class="brand-name">Gilded Vantages</div>
    <div class="offerings"><span>Shutters</span><span>Shades</span><span>Blinds</span></div>
    <div class="emblem-circle"></div>
    <div class="person-name">Daniel Forsythe</div>
    <div class="person-role">Owner</div>
    <div class="divider"></div>
    <ul class="contact-list">
      <li>
        <svg viewBox="0 0 16 16"><path fill="#e3c24f" d="M3 1h3l1.5 4-2 1.3a9 9 0 0 0 4.2 4.2L11 8.5l4 1.5v3a2 2 0 0 1-2 2A12 12 0 0 1 1 3a2 2 0 0 1 2-2z"/></svg>
        919-482-7034
      </li>
      <li>
        <svg viewBox="0 0 16 16"><circle cx="8" cy="8" r="7" fill="none" stroke="#e3c24f" stroke-width="2"/><path d="M1 8h14M8 1c3 3 3 11 0 14M8 1c-3 3-3 11 0 14" fill="none" stroke="#e3c24f" stroke-width="1.3"/></svg>
        gildedvantages.com
      </li>
    </ul>
    <div class="tagline-services">Custom Interior &amp; Exterior<br>Window Treatments</div>
  </article>

  <article class="card card-photo">
    <div class="photo-fill" role="img" aria-label="Greyscale photograph of a home's covered porch with columns and stone wall"></div>
    <div class="brand-name">Gilded Vantages</div>
    <div class="offerings"><span>Shutters</span><span>Shades</span><span>Blinds</span></div>
    <div class="gold-band">Custom Plantation Shutters &amp;<br>Motorized Architectural Shading Systems</div>
  </article>

</body>
</html>
```